Email Signatures

I would like to create a new email signature for my team. The design will be the same for everyone, with only individual details such as name and email changing. You can also see our brand style on our website. https://www.tlmbespokehomes.com.au/

Target Market(s)

Clients for new builds or renovations

Industry/Entity Type

Construction

Colors

Designer to choose colors to be used in the design.

```html
<!DOCTYPE html>
<html lang="en">
<head>
<meta charset="utf-8">
<title>Ashford Lane Homes – Email Signature</title>
<link href="https://fonts.googleapis.com/css2?family=Poppins:wght@400;700;800&display=swap" rel="stylesheet">
<style>
  :root {
    --page-bg: #eceeef;
    --card-bg: #ffffff;
    --brand-green: #129447;
    --ink: #1e1e20;
    --muted: #737373;
  }
  * { box-sizing: border-box; margin: 0; padding: 0; }
  html, body {
    width: 1200px; height: 526px; overflow: hidden;
    background: var(--page-bg);
    font-family: "Poppins", Arial, sans-serif;
  }
  .signature {
    position: absolute; left: 0; top: 111px;
    width: 1200px; height: 304px;
    background: var(--card-bg);
  }
  .brand {
    position: absolute; left: 44px; top: 124px;
    display: flex; align-items: center; gap: 12px;
  }
  .brand-square {
    flex: none;
    width: 20px; height: 20px; background: var(--brand-green);
  }
  .brand-name {
    font-weight: 800; font-size: 23px; line-height: 1.15;
    color: var(--ink); text-transform: uppercase; letter-spacing: 0.3px;
  }
  .person { position: absolute; left: 311px; top: 58px; }
  .person-name {
    font-weight: 700; font-size: 30px; line-height: 1.15;
    color: var(--ink); letter-spacing: -0.2px;
  }
  .person-role {
    font-weight: 400; font-size: 20px; line-height: 1.25;
    color: var(--muted);
  }
  .contacts {
    position: absolute; left: 311px; top: 144px;
    list-style: none;
  }
  .contact {
    display: flex; align-items: center; gap: 9px;
    height: 22px; margin-bottom: 12.5px;
    font-size: 17.5px; line-height: 1; color: var(--muted);
  }
  .contact-icon {
    flex: none;
    width: 22px; height: 22px; border-radius: 3px;
    background: var(--brand-green);
    display: flex; align-items: center; justify-content: center;
  }
  .band-green {
    position: absolute; left: 0; bottom: 0;
    width: 697px; height: 9px; background: var(--brand-green);
    clip-path: polygon(0 0, 100% 0, 99.6% 100%, 0 100%);
  }
  .band-dark {
    position: absolute; right: 0; bottom: 0;
    width: 151px; height: 9px; background: var(--ink);
  }
</style>
</head>
<body>
  <section class="signature">
    <div class="brand">
      <span class="brand-square"></span>
      <span class="brand-name">Ashford Lane<br>Homes</span>
    </div>

    <div class="person">
      <h1 class="person-name">DANIEL J. HARLOW</h1>
      <p class="person-role">Managing Director</p>
    </div>

    <ul class="contacts">
      <li class="contact">
        <span class="contact-icon">
          <svg width="14" height="14" viewBox="0 0 24 24"><path fill="#fff" d="M6.6 10.8a15.1 15.1 0 0 0 6.6 6.6l2.2-2.2c.3-.3.7-.4 1-.2 1.1.4 2.3.6 3.6.6.6 0 1 .4 1 1V20c0 .6-.4 1-1 1C10.6 21 3 13.4 3 4c0-.6.4-1 1-1h3.5c.6 0 1 .4 1 1 0 1.3.2 2.5.6 3.6.1.3 0 .7-.2 1z"/></svg>
        </span>
        +00 123 456 78
      </li>
      <li class="contact">
        <span class="contact-icon">
          <svg width="15" height="12" viewBox="0 0 20 16"><rect x="1" y="1" width="18" height="14" fill="none" stroke="#fff" stroke-width="2"/><path d="M1 1l9 8 9-8M1 15l7-6M19 15l-7-6" fill="none" stroke="#fff" stroke-width="1.8"/></svg>
        </span>
        company@email.com
      </li>
      <li class="contact">
        <span class="contact-icon">
          <svg width="12" height="14" viewBox="0 0 12 16"><path fill="#fff" d="M1 1v12l3-3 2.5 5 2-1-2.5-5H10z"/></svg>
        </span>
        www.ashfordlanehomes.com
      </li>
    </ul>

    <div class="band-green"></div>
    <div class="band-dark"></div>
  </section>
</body>
</html>
```